Company Real Estate Site Needs A Face Lift

I need a new website for the recent company I formed: Brellan Real Estate.
You can use my agent website WWW.PALTUNE.COM to see the style/brand I already have. I will have areas for Searching for homes on QRV, etc.
I really like this site:
http://www.amberfieldhomestead.example/
I have attached my logo as well

Industry/Entity Type

Real Estate

Colors
0255a3
ffffff
cee9f5

```html
<!DOCTYPE html>
<html lang="en">
<head>
<meta charset="utf-8">
<title>Brellan Real Estate</title>
<link rel="stylesheet" href="https://fonts.googleapis.com/css2?family=Cinzel:wght@400;600;700&family=Source+Sans+3:wght@400;600&family=Arimo&display=swap">
<style>
  :root {
    --brand-blue: #0255a3;
    --pale-blue: #cee9f5;
    --gold: #c59a3c;
    --white: #ffffff;
    --ink: #3a3a3a;
    --night: #1c1c1c;
    --band: #010f1e;
    --dot: #8f8f8f;
  }
  * { box-sizing: border-box; margin: 0; padding: 0; }
  html, body { width: 1023px; height: 1200px; overflow: hidden; background: var(--white); }
  .page { position: relative; width: 1023px; height: 1200px; font-family: "Source Sans 3", sans-serif; }
  .top-rule { position: absolute; left: 0; top: 0; width: 100%; height: 7px; background: var(--gold); }
  .brand { position: absolute; left: 0; top: 44px; width: 100%; text-align: center; color: var(--brand-blue); font-weight: 600; }
  .brand-name { display: block; font-size: 52px; line-height: 1; letter-spacing: 1px; }
  .brand-sub { display: block; font-size: 17px; letter-spacing: 6px; margin-top: 6px; }
  .main-nav { position: absolute; top: 158px; left: 0; width: 100%; height: 22px; }
  .main-nav a { position: absolute; font-size: 17px; color: var(--ink); text-decoration: none; }
  .nav-rule { position: absolute; top: 187px; left: 0; width: 100%; height: 5px; background: var(--gold); }
  .hero { position: absolute; top: 192px; left: 0; width: 100%; height: 416px; background: var(--brand-blue); overflow: hidden; }
  .hero-photo { position: absolute; left: 306px; top: 30px; width: 650px; height: 386px;
    background: linear-gradient(to right, rgba(2,85,163,0) 0%, #4a4348 18%, #3a3538 60%, #2a2a30 88%, rgba(2,85,163,0) 100%); }
  .hero-band { position: absolute; left: 0; bottom: 0; width: 100%; height: 48px; background: var(--band); opacity: .93; }
  .hero-title { position: absolute; left: 90px; top: 30px; font-family: "Cinzel", serif; font-weight: 400; font-size: 38px; color: var(--white); letter-spacing: 1px; }
  .hero-title-rule { position: absolute; left: 100px; top: 80px; width: 438px; height: 1px; background: #5b8fd0; }
  .hero-copy { position: absolute; left: 89px; top: 95px; width: 400px; font-size: 15.5px; line-height: 20px; color: var(--white); }
  .hero-button { position: absolute; left: 89px; top: 219px; width: 131px; height: 42px; background: var(--pale-blue); color: #10243a; border-radius: 4px; font-size: 17px; line-height: 42px; text-align: center; }
  .hero-base-rule { position: absolute; top: 608px; left: 0; width: 100%; height: 6px; background: var(--gold); }
  .slider-dots { position: absolute; top: 625px; left: 412px; display: flex; gap: 31px; }
  .slider-dots span { width: 14px; height: 14px; border-radius: 50%; background: var(--dot); }
  .slider-dots .active { background: var(--brand-blue); }
  .service { position: absolute; top: 680px; width: 300px; text-align: center; }
  .service h2 { font-family: "Cinzel", serif; font-weight: 600; font-size: 26px; color: var(--brand-blue); letter-spacing: 1px; }
  .service h3 { font-family: "Cinzel", serif; font-weight: 600; font-size: 14px; color: var(--brand-blue); letter-spacing: 8px; margin-top: 4px; }
  .service p { text-align: left; font-family: "Arimo", sans-serif; font-size: 14.5px; line-height: 17.4px; color: var(--ink); margin: 34px 0 0 38px; width: 235px; }
  .read-more { display: inline-block; margin-top: 27px; width: 104px; height: 33px; line-height: 33px; background: var(--pale-blue); color: var(--ink); border-radius: 3px; font-size: 16px; }
  .divider { position: absolute; top: 695px; width: 2px; height: 252px; background: linear-gradient(to bottom, rgba(197,154,60,0), var(--gold) 30%, var(--gold) 70%, rgba(197,154,60,0)); }
  .link-panel { position: absolute; top: 967px; left: 1px; width: 1022px; height: 149px; background: var(--brand-blue); }
  .link-group { position: absolute; top: 34px; }
  .link-group h4 { font-family: "Cinzel", serif; font-weight: 600; font-size: 15.5px; color: var(--white); letter-spacing: .5px; }
  .link-group a { display: block; font-family: "Arimo", sans-serif; font-size: 12.5px; color: #d9e6f5; text-decoration: none; margin-top: 10px; line-height: 14px; }
  .link-group h4 + a { margin-top: 16px; }
  .footer { position: absolute; top: 1116px; left: 0; width: 100%; height: 84px; background: var(--night); }
  .footer-brand { position: absolute; left: 94px; top: 22px; color: #9a9a9a; font-weight: 600; text-align: center; }
  .footer-brand .brand-name { font-size: 25px; }
  .footer-brand .brand-sub { font-size: 9px; letter-spacing: 3px; margin-top: 3px; }
  .footer-nav a { position: absolute; top: 45px; font-size: 13px; color: #b9b9b9; text-decoration: none; }
  .social { position: absolute; top: 30px; width: 28px; height: 28px; background: var(--gold); }
</style>
</head>
<body>
<div class="page">
  <div class="top-rule"></div>
  <div class="brand">
    <span class="brand-name">BRELLAN</span>
    <span class="brand-sub">REAL ESTATE</span>
  </div>

  <nav class="main-nav">
    <a style="left:91px">HOME</a>
    <a style="left:172px">HOME SEARCH</a>
    <a style="left:310px">BUY</a>
    <a style="left:372px">SELL</a>
    <a style="left:434px">TOURS</a>
    <a style="left:513px">TESTIMONIALS</a>
    <a style="left:648px">HOME BLOG</a>
    <a style="left:759px">RESOURCES</a>
    <a style="left:866px">CONTACT</a>
  </nav>
  <div class="nav-rule"></div>

  <section class="hero">
    <div class="hero-photo" role="img" aria-label="Team photo of six real estate agents in business suits standing with arms crossed"></div>
    <div class="hero-band"></div>
    <h1 class="hero-title">Brellan Real Estate Group</h1>
    <div class="hero-title-rule"></div>
    <p class="hero-copy">Whether you're buying, selling or looking for investment<br>properties, feel free to contact us and we will be<br>happy to help you with all your<br>real estate needs.</p>
    <div class="hero-button">LEARN MORE</div>
  </section>
  <div class="hero-base-rule"></div>

  <div class="slider-dots"><span class="active"></span><span></span><span></span><span></span><span></span></div>

  <section class="service" style="left:66px">
    <h2>BUYING</h2><h3>CONSULTING</h3>
    <p>Lorem ipsum dolor sit amet et aeu consectetur adipiscing elit. Lorem ipsum dolor sit amet consectetur adipiscing elit et loraer sit.<br>Lorem ipsum dolor sitamet et aeu consectetur adipiscing elit sit.</p>
    <span class="read-more">Read more</span>
  </section>
  <div class="divider" style="left:364px"></div>
  <section class="service" style="left:365px">
    <h2>SELLING</h2><h3>SERVICES</h3>
    <p>Lorem ipsum dolor sit amet et aeu consectetur adipiscing elit. Lorem ipsum dolor sit amet consectetur adipiscing elit et loraer sit.<br>Lorem ipsum dolor sitamet et aeu consectetur adipiscing elit sit.</p>
    <span class="read-more">Read more</span>
  </section>
  <div class="divider" style="left:661px"></div>
  <section class="service" style="left:662px">
    <h2>MARKETING</h2><h3>SOLUTIONS</h3>
    <p>Lorem ipsum dolor sit amet et aeu consectetur adipiscing elit. Lorem ipsum dolor sit amet consectetur adipiscing elit et loraer sit.<br>Lorem ipsum dolor sitamet et aeu consectetur adipiscing elit sit.</p>
    <span class="read-more">Read more</span>
  </section>

  <section class="link-panel">
    <div class="link-group" style="left:117px"><h4>INTERESTING LINKS</h4><a>link one goes here</a><a>link two goes here</a></div>
    <div class="link-group" style="left:333px"><h4>MANAGEMENT</h4><a>link one goes here</a><a>link one goes here</a></div>
    <div class="link-group" style="left:549px"><h4>SERVICES</h4><a>link one goes here</a><a>link two goes here</a></div>
    <div class="link-group" style="left:774px"><h4>CONTACT</h4><a>link one goes here</a><a>link two goes here</a></div>
  </section>

  <footer class="footer">
    <div class="footer-brand">
      <span class="brand-name">BRELLAN</span>
      <span class="brand-sub">REAL ESTATE</span>
    </div>
    <nav class="footer-nav">
      <a style="left:293px">HOME</a>
      <a style="left:349px">HOME SEARCH</a>
      <a style="left:450px">HOME VALUE</a>
      <a style="left:540px">COMMUNITY</a>
      <a style="left:629px">MARKET SNAPSHOT</a>
      <a style="left:756px">CONTACT</a>
    </nav>
    <div class="social" style="left:839px" aria-label="Social link"></div>
    <div class="social" style="left:876px" aria-label="Social link"></div>
    <div class="social" style="left:913px" aria-label="Social link"></div>
  </footer>
</div>
</body>
</html>
```